Small consulting business needs a website designed to highlight value and four offerings

My company is a dynamic consulting firm with four Core Offerings: Learning & Evaluation, Program Management, Facilitation & Coaching; Implementation & Transformation. Our mission is to facilitate organizational change and transformation, and to make space for creativity, joy, belonging, and trust. If done successfully, we grow to better understand ourselves, each other, and the work we do together.

I'd like the website to give a feeling of confidence and clarity. I want the colors to match or compliment my logo. I want to have three tabs - Our Clients, Our Services, and Government.

See attached Word document for additional content. My current website is www.BrightHarborGroup.com.

Some websites I'm inspired by:
https://www.ovalmeadowworks.com
https://www.solvantpartnership.com
https://tqrb.org

Some websites of people/groups in my field that I find uninspiring:
http://danaquillby.com
https://www.moorvale.org

Target Market(s)

State and local government agencies, health tech, and corporate HR departments

Industry/Entity Type

public health, aging, government, health tech

Coding

Number of Pages Required

4 page

Font styles to use
Other font styles liked:
• Calibri and Merriweather

Colors
0054AA
0677BA
7BADD7
CADEEF
E8F1F8
00AB8E
00BBA5
67D7C9
C6EFE9
E9F9F6
FFC000
F8CF3A
FAE287
FDF2CF
FEFAEE
F0912C
F2A743
F7CA91
FBE8D2
FDF5EE

Requirements
Must have
• Attached logo and content, water colors few, and photos.
Nice to have
• Real pictures, which I can provide to the chosen designer
Should not have
• AI generated characters or cartoons.

```html
<!DOCTYPE html>
<html lang="en">
<head>
<meta charset="utf-8">
<title>Bright Harbor Group</title>
<link href="https://fonts.googleapis.com/css2?family=Merriweather:wght@300;400;700;900&family=Carlito:wght@400;700&display=swap" rel="stylesheet">
<style>
:root{
  --ink:#143f40;
  --teal:#1f7f74;
  --teal-dark:#0f4446;
  --mint:#bfe9e4;
  --mint-soft:#e6f7f4;
  --olive:#6b8544;
  --olive-dark:#5c763a;
  --gold:#f2b01e;
  --gold-soft:#fbe6a6;
  --cream:#fef8e6;
  --lime:#d8d578;
  --white:#ffffff;
  --text:#3a4447;
}
*{box-sizing:border-box;margin:0;padding:0}
html,body{width:1200px;height:3810px;overflow:hidden}
body{position:relative;background:var(--white);font-family:"Carlito",Calibri,sans-serif;color:var(--text)}
.abs{position:absolute}
.serif{font-family:"Merriweather",Georgia,serif}
.btn{position:absolute;display:flex;align-items:center;justify-content:space-between;padding:0 18px 0 17px;border-radius:4px;background:var(--teal);color:var(--white);font-weight:700;font-size:13px}
.btn::after{content:"";width:7px;height:7px;border-radius:50%;background:currentColor}
.section-title{position:absolute;font-family:"Merriweather",Georgia,serif;font-weight:300;font-size:34px;color:var(--ink);display:flex;align-items:center;gap:8px;white-space:nowrap}
.section-title::after{content:"";width:58px;height:1.5px;background:currentColor}
.body-copy{position:absolute;font-size:12.5px;line-height:17.5px}
.photo{position:absolute;border-radius:50%}

.hero{position:absolute;left:0;top:0;width:1200px;height:680px;background:radial-gradient(ellipse at 20% 30%,#e9f8f5 0,#c9eee8 45%,#b4e6df 75%,#ffffff 100%)}
.logo{position:absolute;left:110px;top:20px;width:136px;text-align:center}
.logo-mark{width:40px;height:40px;border-radius:50%;background:var(--gold);margin:0 auto 12px}
.logo-name{font-family:"Merriweather",Georgia,serif;font-size:15px;line-height:21px;color:var(--ink)}
.nav{position:absolute;top:44px;font-size:13px;color:var(--ink)}
.nav-contact{position:absolute;left:965px;top:35px;width:112px;height:33px;border:1.5px solid var(--teal);border-radius:4px;display:flex;align-items:center;justify-content:space-between;padding:0 14px;font-size:13px;color:var(--ink)}
.nav-contact::after{content:"";width:7px;height:7px;border-radius:50%;background:var(--teal)}
.eyebrow{position:absolute;left:123px;top:218px;font-size:12px;color:var(--gold);display:flex;align-items:center;gap:8px}
.eyebrow::after{content:"";width:84px;height:1px;background:var(--gold)}
.hero-title{position:absolute;left:122px;top:240px;width:560px;font-family:"Merriweather",Georgia,serif;font-weight:300;font-size:38px;line-height:45px;color:var(--ink);white-space:nowrap}
.hero-lead{position:absolute;left:123px;top:390px;width:470px;font-size:12px;line-height:22px;color:var(--ink)}
.hero-lead span{font-size:15.5px}
.hero-art{position:absolute;left:655px;top:130px;width:420px;height:420px;border-radius:50%;background:radial-gradient(circle at 45% 40%,#f3cd4a 0,#9fb552 40%,#4f9884 70%,#d6efe8 100%)}

.edge{position:absolute;left:0;width:1200px}

.green-band{position:absolute;left:0;top:1120px;width:1200px;height:480px;background:var(--olive)}
.help{position:absolute;left:0;top:1990px;width:1200px;height:540px;background:linear-gradient(#ffffff 0,var(--cream) 25%,var(--gold-soft) 85%,#f8d98a 100%)}
.help-kicker{position:absolute;left:0;width:1200px;top:2134px;text-align:center;font-family:"Merriweather",Georgia,serif;font-weight:300;font-size:31px;color:var(--ink)}
.help-line{position:absolute;left:0;width:1200px;text-align:center;font-family:"Merriweather",Georgia,serif;font-weight:700;font-size:76px;line-height:90px;color:var(--ink);white-space:nowrap}
.inline-photo{display:inline-block;width:92px;height:92px;border-radius:50%;vertical-align:middle;margin:0 14px;position:relative;top:-8px}

.collab-title{position:absolute;left:0;width:1200px;top:2577px;text-align:center;font-family:"Merriweather",Georgia,serif;font-weight:300;font-size:34px;color:var(--ink)}
.collab-sub{position:absolute;left:0;width:1200px;top:2624px;text-align:center;font-size:14px;color:var(--teal)}
.collab-photo{position:absolute;left:494px;top:2657px;width:216px;height:216px;border-radius:50%;background:radial-gradient(circle at 50% 45%,#c9a98a,#7d7a78 60%,#5b6d72)}
.partner{position:absolute;font-size:16px;color:var(--ink);white-space:nowrap}
.partner-icon{position:absolute;width:50px;height:50px;border-radius:50%;background:var(--mint-soft);display:flex;align-items:center;justify-content:center}
.partner-icon i{width:22px;height:22px;border-radius:5px;background:linear-gradient(135deg,var(--gold),var(--teal))}

.why-box{position:absolute;left:577px;top:3090px;width:531px;height:358px;background:var(--lime)}

.footer{position:absolute;left:0;top:3500px;width:1200px;height:310px;background:var(--teal-dark);color:var(--white)}
.foot-head{position:absolute;top:3585px;font-family:"Merriweather",Georgia,serif;font-size:14px;font-weight:400;color:var(--white)}
.foot-link{position:absolute;font-size:9.5px;color:#dfeeed}
.foot-rule{position:absolute;top:3588px;width:1px;height:150px;background:rgba(255,255,255,.25)}
.foot-icon{position:absolute;width:20px;height:20px;border-radius:50%;border:1px solid #dfeeed;display:flex;align-items:center;justify-content:center}
.foot-icon svg{width:11px;height:11px}
.email-field{position:absolute;left:901px;top:3616px;width:176px;height:32px;border:1px solid #dfeeed;border-radius:3px;font-size:9.5px;padding:10px 12px;color:#dfeeed}
.subscribe{left:901px;top:3661px;width:126px;height:37px}
.copyright{position:absolute;left:0;width:1200px;top:3786px;text-align:center;font-size:8.5px;color:#dfeeed}
</style>
</head>
<body>

<section class="hero">
  <div class="logo">
    <div class="logo-mark"></div>
    <div class="logo-name">Bright Harbor<br>Group</div>
  </div>
  <nav>
    <span class="nav" style="left:652px">Our Clients</span>
    <span class="nav" style="left:751px">Our Services</span>
    <span class="nav" style="left:858px">Government</span>
    <span class="nav-contact">Contact Us</span>
  </nav>

  <div class="eyebrow">Welcome To Bright Harbor Group</div>
  <h1 class="hero-title">A Seat at the Table for<br>Collaboration, Learning<br>and Meaningful Change.</h1>
  <p class="hero-lead">Bright Harbor Group is a dynamic consulting firm with four Core<br><span>Offerings: Learning &amp; Evaluation, Program Management,<br>Facilitation &amp; Coaching; Implementation &amp; Transformation</span></p>
  <div class="btn" style="left:123px;top:477px;width:169px;height:39px">Explore Our Services</div>

  <div class="hero-art" role="img" aria-label="Watercolour illustration presenting the four core offerings"></div>
</section>

<svg class="edge" style="top:620px" height="70" viewBox="0 0 1200 70" preserveAspectRatio="none">
  <path d="M0,30 L40,22 L80,34 L130,18 L190,30 L250,20 L320,32 L400,16 L470,28 L540,20 L620,34 L700,22 L780,30 L860,18 L940,32 L1020,20 L1100,30 L1200,22 L1200,70 L0,70 Z" fill="#ffffff"/>
</svg>

<div class="help"></div>

<section>
  <div class="photo" role="img" aria-label="Photo of a climber reaching a target at sunset" style="left:318px;top:712px;width:296px;height:320px;background:radial-gradient(circle at 55% 50%,#f2a743,#7a5a3a 60%,#2d2a28)"></div>
  <div class="photo" role="img" aria-label="Watercolour illustration of a road leading to a horizon" style="left:202px;top:822px;width:186px;height:186px;border:6px solid #fff;background:radial-gradient(circle at 50% 40%,#f8cf3a,#5aa596 65%,#2e6b70)"></div>
  <h2 class="section-title" style="left:750px;top:768px">Our Mission</h2>
  <p class="body-copy" style="left:751px;top:820px;width:285px">Our mission is to facilitate organizational change and transformation, and to make space for creativity, joy, belonging, and trust. If done successfully, we grow to better understand ourselves, each other, and the work we do together.</p>
  <div class="btn" style="left:753px;top:934px;width:169px;height:40px">Read Our Mission</div>
</section>

<svg class="edge" style="top:1095px" height="40" viewBox="0 0 1200 40" preserveAspectRatio="none">
  <path d="M0,28 L60,16 L120,24 L200,12 L280,26 L360,14 L440,24 L520,10 L600,22 L690,12 L780,26 L860,14 L940,24 L1030,12 L1110,24 L1200,14 L1200,40 L0,40 Z" fill="#6b8544"/>
</svg>
<div class="green-band"></div>
<svg class="edge" style="top:1595px" height="40" viewBox="0 0 1200 40" preserveAspectRatio="none">
  <path d="M0,0 L1200,0 L1200,16 L1120,28 L1040,14 L960,26 L880,12 L800,24 L720,14 L640,28 L560,16 L480,26 L400,12 L320,24 L240,14 L160,26 L80,14 L0,24 Z" fill="#6b8544"/>
</svg>
<section>
  <h2 class="section-title" style="left:178px;top:1264px;color:#fff">Our Vision</h2>
  <p class="body-copy" style="left:179px;top:1316px;width:285px;color:#f3f5ec">Our vision is to be part of a world where organizations and collaborators connect as human beings first. We envision a future where partners and colleagues strive for ongoing growth together.</p>
  <div class="btn" style="left:180px;top:1413px;width:150px;height:40px;background:var(--gold)">View Our Vision</div>
  <div class="photo" role="img" aria-label="Photo of a presenter leading a team meeting beside a vision board" style="left:592px;top:1206px;width:330px;height:318px;background:radial-gradient(circle at 50% 45%,#d9e6ef,#8aa7bf 60%,#4e5f6c)"></div>
  <div class="photo" role="img" aria-label="Watercolour illustration of a rising sun over waves" style="left:812px;top:1292px;width:168px;height:168px;border:8px solid var(--olive-dark);background:radial-gradient(circle at 60% 35%,#f8cf3a,#67b4a6 60%,#2b6d6e)"></div>
</section>

<section>
  <div class="photo" role="img" aria-label="Photo of a hand placing letter blocks on a table" style="left:286px;top:1665px;width:306px;height:363px;background:radial-gradient(circle at 55% 50%,#e9dcc9,#9d8a74 60%,#4b4a52)"></div>
  <div class="photo" role="img" aria-label="Watercolour illustration of interlocking circles" style="left:180px;top:1780px;width:184px;height:184px;border:6px solid #fff;background:radial-gradient(circle,#f8cf3a,#6db7a9 60%,#dfeee8)"></div>
  <h2 class="section-title" style="left:728px;top:1727px">Our Value</h2>
  <p class="body-copy" style="left:729px;top:1778px;width:310px">We are the tranquility in chaos. The steady partner always at the table with you. We drive meaningful and measurable change, resulting in sustained progress towards key community outcomes and multi-sector initiatives. Our work produces values realignment, critical technical assistance, and develops strategic plans for innovative organizations ready to elevate their work.</p>
  <div class="btn" style="left:731px;top:1927px;width:127px;height:40px">Learn More</div>
</section>

<section>
  <p class="help-kicker">We Help Your Team...</p>
  <p class="help-line" style="top:2196px">Turn Bold <span class="inline-photo" role="img" aria-label="Watercolour emblem of linked shapes" style="background:radial-gradient(circle,#f8cf3a,#4c9b8f 70%)"></span>Visions</p>
  <p class="help-line" style="top:2286px">into <span class="inline-photo" role="img" aria-label="Watercolour illustration of a sun over waves" style="background:radial-gradient(circle at 55% 35%,#f8cf3a,#5aa596 65%)"></span>Practical Results.</p>
  <svg class="abs" style="left:562px;top:2408px" width="76" height="26" viewBox="0 0 76 26" fill="none" stroke="#143f40" stroke-width="1.4">
    <circle cx="13" cy="13" r="11"/><path d="M7,13 H36 M11,9 L7,13 L11,17"/>
    <circle cx="63" cy="13" r="11"/><path d="M40,13 H69 M65,9 L69,13 L65,17"/>
  </svg>
</section>
<svg class="edge" style="top:2510px" height="40" viewBox="0 0 1200 40" preserveAspectRatio="none">
  <path d="M0,0 L1200,0 L1200,14 L1110,26 L1020,12 L940,24 L850,14 L760,28 L680,14 L600,26 L510,12 L430,24 L340,14 L260,26 L170,12 L90,24 L0,14 Z" fill="#f8d98a"/>
</svg>

<section>
  <h2 class="collab-title">We Collaborate With</h2>
  <p class="collab-sub">Deviate more here Between Nonprofit and Corporate</p>
  <div class="collab-photo" role="img" aria-label="Illustrated photo of a team joining hands"></div>
  <span class="partner" style="right:774px;top:2700px">Foundations</span>
  <div class="partner-icon" style="left:438px;top:2682px"><i></i></div>
  <span class="partner" style="left:771px;top:2699px">Startups in tech</span>
  <div class="partner-icon" style="left:706px;top:2682px"><i></i></div>
  <span class="partner" style="right:796px;top:2792px">Large-scale Companies</span>
  <div class="partner-icon" style="left:417px;top:2777px"><i></i></div>
  <span class="partner" style="left:792px;top:2792px">State Government agencies</span>
  <div class="partner-icon" style="left:730px;top:2777px"><i></i></div>
  <span class="partner" style="right:752px;top:2884px">National and local Nonprofits</span>
  <div class="partner-icon" style="left:460px;top:2869px"><i></i></div>
  <span class="partner" style="left:747px;top:2890px">Tribal Serving-Organizations</span>
  <div class="partner-icon" style="left:684px;top:2875px"><i></i></div>
  <div class="partner-icon" style="left:574px;top:2910px"><i></i></div>
  <span class="partner" style="left:0;width:1200px;text-align:center;top:2970px">International Partnerships &amp; Organizations</span>
</section>

<section>
  <div class="why-box"></div>
  <div class="abs" role="img" aria-label="Photo of a hand holding a network of connected circles over a city" style="left:121px;top:3052px;width:532px;height:359px;background:linear-gradient(135deg,#a9d6e6 0,#3f7c96 45%,#123c4f 100%)"></div>
  <h2 class="section-title" style="left:709px;top:3135px">Why Us</h2>
  <p class="body-copy" style="left:709px;top:3186px;width:342px;font-size:11.5px;line-height:17.3px">Through our Core Offerings and guided by our founder's traditional and nontraditional methods for engaging and steering a team, we create a sense of belonging, foster transparency, and help to build stronger relationships. Our approach helps to drive meaningful change so that organizations and initiatives can clear roadblocks and meet collective goals. Our team's proven ability to transform conflict into opportunity will help to advance your organization and the communities you serve.</p>
  <div class="btn" style="left:709px;top:3355px;width:127px;height:36px">Learn More</div>
</section>

<svg class="edge" style="top:3470px" height="40" viewBox="0 0 1200 40" preserveAspectRatio="none">
  <path d="M0,24 L70,12 L150,26 L230,10 L320,22 L400,12 L490,26 L570,14 L660,24 L740,10 L830,24 L910,14 L1000,26 L1080,12 L1200,22 L1200,40 L0,40 Z" fill="#0f4446"/>
</svg>
<footer class="footer"></footer>
<section>
  <div class="abs" style="left:97px;top:3592px;width:200px;text-align:center">
    <div style="width:52px;height:52px;border-radius:50%;background:var(--gold);margin:0 auto 28px"></div>
    <div class="serif" style="font-size:20px;line-height:30px;color:#fff">Bright Harbor<br>Group</div>
  </div>
  <div class="foot-rule" style="left:317px"></div>
  <div class="foot-rule" style="left:485px"></div>
  <div class="foot-rule" style="left:687px"></div>
  <div class="foot-rule" style="left:873px"></div>

  <h3 class="foot-head" style="left:361px">Main Links</h3>
  <span class="foot-link" style="left:362px;top:3620px">Home</span>
  <span class="foot-link" style="left:362px;top:3642px">Our Clients</span>
  <span class="foot-link" style="left:362px;top:3665px">Our Services</span>
  <span class="foot-link" style="left:362px;top:3688px">Government</span>

  <h3 class="foot-head" style="left:515px">Contact Us</h3>
  <div class="foot-icon" style="left:515px;top:3616px"><svg viewBox="0 0 12 12" fill="none" stroke="#fff" stroke-width="1.2"><path d="M6,11 C3,7 2.5,5.8 2.5,4.5 A3.5,3.5 0 0 1 9.5,4.5 C9.5,5.8 9,7 6,11 Z"/><circle cx="6" cy="4.5" r="1.2"/></svg></div>
  <span class="foot-link" style="left:543px;top:3615px;width:130px;line-height:11px">Fairhaven Bay, SC, United States, South Carolina</span>
  <div class="foot-icon" style="left:515px;top:3648px"><svg viewBox="0 0 12 12" fill="none" stroke="#fff" stroke-width="1.2"><path d="M2,2 L4.5,1.5 L5.5,4 L4,5 C4.8,6.6 5.4,7.2 7,8 L8,6.5 L10.5,7.5 L10,10 C5.5,10 2,6.5 2,2 Z"/></svg></div>
  <span class="foot-link" style="left:543px;top:3652px">+1 555 014 2290</span>
  <div class="foot-icon" style="left:515px;top:3681px"><svg viewBox="0 0 12 12" fill="none" stroke="#fff" stroke-width="1.2"><rect x="1.5" y="3" width="9" height="6.5"/><path d="M1.5,3 L6,7 L10.5,3"/></svg></div>
  <span class="foot-link" style="left:543px;top:3685px;color:var(--gold)">Info@BrightHarborGroup.com</span>

  <h3 class="foot-head" style="left:744px">Follow us</h3>
  <div class="foot-icon" style="left:744px;top:3616px"></div>
  <span class="foot-link" style="left:775px;top:3620px">Facepage</span>
  <div class="foot-icon" style="left:744px;top:3648px"></div>
  <span class="foot-link" style="left:775px;top:3652px">Snapgram</span>
  <div class="foot-icon" style="left:744px;top:3681px"></div>
  <span class="foot-link" style="left:775px;top:3685px">Chirper</span>

  <h3 class="foot-head" style="left:898px">Subscribe Newsletter</h3>
  <div class="email-field">Enter Your Email</div>
  <div class="btn subscribe">Subscribe</div>

  <div class="abs" style="left:32px;top:3767px;width:1136px;height:1px;background:rgba(255,255,255,.25)"></div>
  <p class="copyright">© 2025 Bright Harbor Group All Rights Reserved.</p>
</section>

</body>
</html>
```